Custom workshop/manufacture for custom furniture, architectural millwork and kitchen cabinetry

simple and clean. I like this website:
http://www.pebblelarchworks.com

Attached are random ideas

Target Market(s)

residential, commercial, hospitality, interior designers, architects, contractors

Coding

Coded - Design and coding required

Number of Pages Required

5+ page

Font styles to use
Other font styles liked:
• Avenir next

Requirements
Must have
• drop down menu for work - residential - commercial

```html
<!DOCTYPE html>
<html lang="en">
<head>
<meta charset="utf-8">
<title>Hollin Vale Joinery — Woodwork and Interiors</title>
<link href="https://fonts.googleapis.com/css2?family=Open+Sans:wght@400;600;700&family=Oswald:wght@400;500&family=Quicksand:wght@500&family=Montserrat:wght@500&display=swap" rel="stylesheet">
<style>
  :root {
    --ink: #2b2b2b;
    --bar: #2e2e2e;
    --black: #111111;
    --white: #ffffff;
    --muted: #8a8a8a;
    --card: #eef1f5;
    --line: #d9d9d9;
    --cream: #fbfbf3;
    --wood-a: #cbb89a;
    --wood-b: #8f7a5c;
  }
  * { box-sizing: border-box; margin: 0; padding: 0; }
  html, body { width: 1200px; height: 2446px; overflow: hidden; background: var(--white); }
  body { font-family: "Open Sans", sans-serif; color: var(--ink); }
  .page { position: relative; width: 1200px; height: 2446px; overflow: hidden; }
  .abs { position: absolute; }

  /* header */
  .brand { left: 80px; top: 34px; font: 600 24px/1.1 "Open Sans", sans-serif; color: var(--ink); width: 170px; }
  .social { right: 80px; top: 36px; display: flex; gap: 16px; }
  .social span { width: 14px; height: 14px; border-radius: 50%; background: var(--ink); display: block; }
  .phone { right: 80px; top: 72px; font: 400 24px "Oswald", sans-serif; letter-spacing: 1px; }

  /* hero */
  .hero { left: 0; top: 157px; width: 1200px; height: 404px;
    background: linear-gradient(100deg, #a9a79b 0%, #d8d0c0 30%, #b59d78 60%, #7d6648 100%); }
  .hero-title { left: 0; width: 1200px; top: 306px; text-align: center; color: var(--white);
    font: 700 46px "Open Sans", sans-serif; letter-spacing: 1px; }
  .hero-sub { left: 0; width: 1200px; top: 366px; text-align: center; color: var(--white); font: 400 24px "Open Sans", sans-serif; }
  .arrow { top: 327px; width: 44px; height: 74px; background: var(--black); display: flex; align-items: center; justify-content: center; }

  /* nav */
  .nav { left: 80px; top: 127px; width: 1040px; height: 55px; background: var(--bar); display: flex; }
  .nav a { color: var(--white); text-decoration: none; font: 400 15px "Oswald", sans-serif; padding: 0 26px;
    line-height: 55px; border-right: 1px solid #444; }
  .nav .enquiry { margin-left: auto; background: var(--black); border: none; width: 153px; text-align: center; padding: 0; }

  /* about */
  .about-bg { left: 0; top: 632px; width: 1200px; height: 708px;
    background: linear-gradient(180deg, #d7d6d1 0%, #c8c3b8 70%, var(--wood-a) 80%, var(--wood-b) 100%); }
  .about-veil { left: 0; top: 632px; width: 1200px; height: 584px; background: rgba(247,247,247,.88); }
  .about-title { left: 152px; top: 890px; font: 700 32px "Open Sans", sans-serif; color: #3a3a3a; }
  .about-rule { left: 378px; top: 683px; width: 1px; height: 497px; background: var(--line); }
  .about-text { left: 414px; top: 676px; width: 706px; font: 500 13.6px/23px "Quicksand", sans-serif; color: #3b3b3b; }
  .about-text p { margin-bottom: 23px; }

  /* testimonials */
  .section-title { font: 500 19px "Montserrat", sans-serif; letter-spacing: 1px; }
  .t-title { left: 0; width: 1200px; top: 1396px; text-align: center; }
  .t-rule { left: 586px; top: 1424px; width: 28px; height: 3px; background: var(--ink); }
  .t-card { top: 1461px; width: 498px; height: 109px; background: var(--card); padding: 16px 36px;
    text-align: center; font: 400 12.5px/20px "Open Sans", sans-serif; color: var(--muted); }
  .avatar { width: 90px; height: 90px; border-radius: 50%; border: 3px solid var(--white); background: linear-gradient(160deg, #c9b8a6, #6e7f92); }
  .t-name { font: 600 13px "Open Sans", sans-serif; color: #444; }
  .t-role { font: 400 12.5px "Open Sans", sans-serif; color: var(--muted); }

  /* contact */
  .contact-bg { left: 0; top: 1700px; width: 1200px; height: 500px; background: var(--cream); }
  .c-title { left: 80px; top: 1737px; font: 700 19px "Open Sans", sans-serif; }
  .c-rule { left: 80px; top: 1765px; width: 30px; height: 3px; background: var(--ink); }
  .field { left: 80px; width: 420px; height: 40px; background: var(--white); border: 1px solid var(--line);
    font: 400 12.5px "Open Sans", sans-serif; color: #555; padding: 11px 12px; }
  .submit { left: 80px; top: 2079px; width: 99px; height: 40px; background: var(--bar); color: var(--white);
    font: 700 12.5px/40px "Open Sans", sans-serif; text-align: center; }
  .plan { left: 620px; top: 1730px; width: 500px; height: 420px;
    background: radial-gradient(closest-side, #e2d6c5 0%, #d6cab8 55%, rgba(251,251,243,0) 100%); }

  /* footer */
  .footer { left: 0; top: 2200px; width: 1200px; height: 246px; background: linear-gradient(180deg, #1b1c22, #101114); }
  .f-brand { left: 80px; top: 2244px; width: 126px; height: 80px; background: var(--white); color: var(--ink);
    font: 600 15px/1.2 "Open Sans", sans-serif; padding: 14px 10px; }
  .f-legal { left: 84px; top: 2346px; color: var(--white); font: 400 11px/18px "Open Sans", sans-serif; }
  .f-head { top: 2242px; color: var(--white); font: 400 17px "Oswald", sans-serif; }
  .f-head::after { content: ""; display: block; width: 34px; height: 1px; background: #888; margin-top: 4px; }
  .f-list { left: 390px; top: 2282px; list-style: none; color: var(--white); font: 400 12.5px/25px "Open Sans", sans-serif; }
  .f-list li::before { content: "›"; margin-right: 10px; }
  .f-contact { left: 555px; color: var(--white); font: 400 12.5px/18px "Open Sans", sans-serif; display: flex; gap: 10px; }
</style>
</head>
<body>
<div class="page">

  <header>
    <div class="abs brand">Hollin Vale Joinery</div>
    <div class="abs social" aria-label="Social links"><span></span><span></span><span></span><span></span></div>
    <div class="abs phone">(123) 456-7890</div>
  </header>

  <section>
    <div class="abs hero" role="img" aria-label="Photograph of a bright living room with a wooden media wall"></div>
    <h1 class="abs hero-title">WOODWORK AND INTERIORS</h1>
    <p class="abs hero-sub">Handcrafted in Brooklyn</p>
    <div class="abs arrow" style="left:60px"><svg width="12" height="14" viewBox="0 0 12 14"><path d="M8 2 3 7l5 5" fill="none" stroke="#fff" stroke-width="2.5"/></svg></div>
    <div class="abs arrow" style="left:1096px"><svg width="12" height="14" viewBox="0 0 12 14"><path d="M4 2l5 5-5 5" fill="none" stroke="#fff" stroke-width="2.5"/></svg></div>
  </section>

  <nav class="abs nav">
    <a href="#">HOME</a><a href="#">ABOUT US</a><a href="#">SERVICES</a><a href="#">GALLERY</a><a href="#">CONTACT US</a>
    <a href="#" class="enquiry">ENQUIRY NOW</a>
  </nav>

  <section>
    <div class="abs about-bg" role="img" aria-label="Photograph of an open interior with large windows and a wooden floor"></div>
    <div class="abs about-veil"></div>
    <h2 class="abs about-title">ABOUT US</h2>
    <div class="abs about-rule"></div>
    <div class="abs about-text">
      <p>Lorem ipsum dolor sit amet, consectetur adipiscing elit. Nulla vehicula malesuada nisi eu rutrum. Maecenas purus diam, lobortis at velit eget, ultricies posuere augue. Nullam nec lectus a augue dictum euismod ut sed ex. Integer pretium arcu neque, vitae mollis massa consequat eu. In eget dolor luctus, varius dui fringilla, lobortis odio. Cras molestie nunc pretium, dictum lorem vel, vulputate mi. Etiam ac ligula bibendum, luctus diam sit amet, rutrum ipsum.</p>
      <p>Praesent tempus at neque non hendrerit. In euismod vestibulum sodales. Fusce feugiat dapibus facilisis. Sed interdum mauris sed vulputate fringilla. Sed purus dui, tempus tempor velit vel, feugiat eleifend nulla.</p>
      <p>Lorem ipsum dolor sit amet, consectetur adipiscing elit. Nulla vehicula malesuada nisi eu rutrum. Maecenas purus diam, lobortis at velit eget, ultricies posuere augue. Nullam nec lectus a augue dictum euismod ut sed ex. Integer pretium arcu neque, vitae mollis massa consequat eu. In eget dolor luctus, varius dui fringilla, lobortis odio. Cras molestie nunc pretium, dictum lorem vel, vulputate mi. Etiam ac ligula bibendum, luctus diam sit amet, rutrum ipsum.</p>
      <p>Praesent tempus at neque non hendrerit. In euismod vestibulum sodales. Fusce feugiat dapibus facilisis. Sed interdum mauris sed vulputate fringilla. Sed purus dui, tempus tempor velit vel, feugiat eleifend nulla [...] Lorem ipsum dolor sit amet, consectetur adipiscing elit. Nulla vehicula malesuada nisi eu rutrum. Maecenas purus diam, lobortis at velit eget, ultricies posuere augue. Nullam nec lectus a augue dictum euismod ut sed ex. Integer pretium arcu neque, vitae mollis massa consequat eu. In eget dolor luctus, varius dui fringilla, lobortis odio. Cras molestie nunc pretium, dictum lorem vel, vulputate mi. Etiam ac ligula bibendum, luctus diam sit amet, rutrum ipsum.</p>
    </div>
  </section>

  <section>
    <h2 class="abs section-title t-title">TESTIMONIAL</h2>
    <div class="abs t-rule"></div>

    <blockquote class="abs t-card" style="left:80px">Lorem ipsum dolor sit amet, consectetur adipiscing elit. Phasellus sagittis bibendum ultricies. Curabitur vel pellentesque turpis. Integer sed arcu ullamcorper, rhoncus purus et, faucibus dolor.</blockquote>
    <div class="abs avatar" style="left:92px;top:1545px" role="img" aria-label="Portrait photo of the client"></div>
    <div class="abs t-name" style="left:205px;top:1587px">Dana Whitfield</div>
    <div class="abs t-role" style="left:205px;top:1612px">Nullam tempus</div>

    <blockquote class="abs t-card" style="left:621px">Lorem ipsum dolor sit amet, consectetur adipiscing elit. Phasellus sagittis bibendum ultricies. Curabitur vel pellentesque turpis. Integer sed arcu ullamcorper, rhoncus purus et, faucibus dolor.</blockquote>
    <div class="abs avatar" style="left:633px;top:1545px" role="img" aria-label="Portrait photo of the client"></div>
    <div class="abs t-name" style="left:746px;top:1587px">Lena Marsh</div>
    <div class="abs t-role" style="left:746px;top:1612px">Nullam tempus</div>
  </section>

  <section>
    <div class="abs contact-bg"></div>
    <h2 class="abs c-title">CONTACT</h2>
    <div class="abs c-rule"></div>
    <div class="abs field" style="top:1797px">Name</div>
    <div class="abs field" style="top:1851px">Email</div>
    <div class="abs field" style="top:1906px">Phone</div>
    <div class="abs field" style="top:1960px;height:96px">Message</div>
    <div class="abs submit">SUBMIT</div>
    <div class="abs plan" role="img" aria-label="Isometric illustration of a furnished apartment floor plan"></div>
  </section>

  <footer>
    <div class="abs footer" role="img" aria-label="Dim evening photograph of a modern house"></div>
    <div class="abs f-brand">Hollin Vale Joinery</div>
    <div class="abs f-legal">Company Name © 2018. All Rights Reserved<br>Terms of Use and Privacy Policy</div>
    <div class="abs f-head" style="left:390px">Menu</div>
    <ul class="abs f-list"><li>Home</li><li>About us</li><li>Services</li><li>Gallery</li><li>Contact us</li></ul>
    <div class="abs f-head" style="left:551px">Contact</div>
    <div class="abs f-contact" style="top:2284px">
      <svg width="10" height="14" viewBox="0 0 10 14"><path d="M5 0a5 5 0 0 0-5 5c0 4 5 9 5 9s5-5 5-9a5 5 0 0 0-5-5zm0 7a2 2 0 1 1 0-4 2 2 0 0 1 0 4z" fill="#fff"/></svg>
      <span>123 Lorem Ipsum Dolor,<br>Sit Ameut elit.</span>
    </div>
    <div class="abs f-contact" style="top:2334px">
      <svg width="12" height="12" viewBox="0 0 12 12"><path d="M2.5 0 4.5 3 3.3 4.4a7 7 0 0 0 4.3 4.3L9 7.5l3 2-1.2 2.2C5.5 12 0 6.5.3 1.2z" fill="#fff"/></svg>
      <span>(123) 456-7890</span>
    </div>
  </footer>

</div>
</body>
</html>
```